RO Interiors Website Re-Design

I am an interior designer. What I do, is work with customers to design spaces in their homes prior to a contractor doing the work. This could be kitchens, bathrooms, offices, and more. I have uploaded a file, and it has my URL within it for you to use as a reference.
https://rointeriors-studio.example/

Industry/Entity Type

Interior Design

Coding

Coded - Design and coding required

Number of Pages Required

5+ page

Requirements
Must have
• Clean, professional, easy to navigate, color schemes should follow what is on my current site, also written content you can pull from my current site as well along with the current script / font

```html
<!DOCTYPE html>
<html lang="en">
<head>
<meta charset="utf-8">
<title>RO Interiors – Landing Page, Mobile View</title>
<link href="https://fonts.googleapis.com/css2?family=Nunito:wght@400;600;700;800&family=Roboto:wght@500;700&display=swap" rel="stylesheet">
<style>
  :root{
    --bg:#f0f0f0;
    --ink:#2b2b2b;
    --dark:#2c2e31;
    --dark-2:#3a3330;
    --gold:#e8c21b;
    --white:#ffffff;
    --muted:#c9c9c9;
    --line:#d9d9d9;
  }
  *{box-sizing:border-box;margin:0;padding:0}
  html,body{width:1200px;height:921px;overflow:hidden;background:var(--bg)}
  body{position:relative;font-family:"Nunito",sans-serif;color:var(--ink)}

  .intro-brand{position:absolute;left:30px;top:180px;font-family:"Nunito",sans-serif;font-weight:400;font-size:40px;letter-spacing:1px;color:var(--ink)}
  .intro-title{position:absolute;left:26px;top:276px;font-family:"Roboto",sans-serif;font-weight:700;font-size:60px;color:var(--ink);letter-spacing:-0.5px}
  .intro-sub{position:absolute;left:27px;top:370px;font-family:"Roboto",sans-serif;font-weight:700;font-size:29px;color:var(--ink)}
  .intro-band{position:absolute;left:0;top:537px;width:380px;height:384px;background:var(--dark);border-top-right-radius:110px}
  .intro-badge{position:absolute;left:256px;top:510px;width:106px;height:106px;border-radius:50%;background:var(--white)}

  .screen{position:absolute;width:158px;overflow:hidden;background:var(--white)}
  .screen-home{left:463px;top:61px;height:860px;border-radius:8px 8px 0 0}
  .screen-about{left:694px;top:0;height:921px}
  .screen-footer{left:925px;top:0;height:837px;border-radius:0 0 8px 8px}
  .abs{position:absolute}
  .center{left:0;right:0;text-align:center}
  .photo{position:absolute}
  .dark{position:absolute;left:0;right:0;background:var(--dark)}
  .gold{color:var(--gold)}
  .white{color:var(--white)}

  .site-logo{font-size:9px;letter-spacing:.3px;color:var(--ink)}
  .burger{position:absolute;right:10px;top:12px;width:8px}
  .burger span{display:block;height:1px;background:var(--ink);margin-bottom:2px}

  .hero-welcome{font-size:11.5px;font-weight:600}
  .hero-big{font-size:22px;font-weight:800;letter-spacing:.3px}
  .hero-rule{position:absolute;left:42px;width:74px;height:1.5px;background:var(--gold)}
  .social-rail{position:absolute;right:0;top:219px;width:21px;height:118px;background:var(--dark);border-radius:4px 0 0 4px}
  .social-rail i{position:absolute;left:6px;width:9px;height:9px;border:1px solid var(--muted);border-radius:50%}

  .body-copy{font-size:8.4px;line-height:1.6;font-weight:600}
  .btn{position:absolute;background:var(--dark);color:var(--white);border-radius:2px;text-align:center}
  .btn-lg{font-size:7.6px;line-height:22px;height:22px}
  .btn-sm{font-size:4.4px;line-height:13px;height:13px}

  .eyebrow{font-size:6px;font-weight:700}
  .lead-title{font-size:9.5px;line-height:1.5}
  .caption{font-size:4.4px;line-height:1.6}
  .dots{position:absolute;background-image:radial-gradient(#777 0.6px,transparent 0.7px);background-size:4px 4px}

  .why-label{font-size:7px;font-weight:700}
  .why-heading{font-size:11.2px;line-height:1.35}
  .check{position:absolute;left:14px;font-size:5px;display:flex;align-items:center;gap:5px}
  .check svg{width:8px;height:8px}

  .services-bg{background:linear-gradient(180deg,#3a3431 0%,#4a3a33 30%,#3b3532 60%,#2f2d2e 100%)}
  .svc-title{font-size:11.5px;font-weight:700}
  .svc-lead{font-size:11px;line-height:1.6}
  .svc-name{font-size:11px;font-weight:700;letter-spacing:.2px}
  .svc-copy{font-size:8px;line-height:1.6}
  .see-more{font-size:8.2px}

  .port-title{font-size:11.5px;font-weight:600}
  .port-copy{font-size:11.4px;line-height:1.55}
  .carousel-label{font-size:7.5px;font-weight:700}
  .arrow-dot{position:absolute;width:8px;height:8px;border:1px solid var(--gold);border-radius:50%}

  .foot-small{font-size:4.6px;line-height:1.6}
  .input{position:absolute;height:12px;border:1px solid var(--line);font-size:4.4px;line-height:10px;padding-left:4px;color:#aaa}
  .foot-head{font-size:10px;letter-spacing:.2px}
  .foot-link{font-size:7.2px;line-height:16.5px;white-space:nowrap}
  .foot-rule{position:absolute;left:0;right:0;height:1px;background:#55585c}
</style>
</head>
<body>

  <div class="intro-brand">RO INTERIORS</div>
  <div class="intro-title">Landing Page</div>
  <div class="intro-sub">Mobile View</div>
  <div class="intro-band"></div>
  <div class="intro-badge" role="img" aria-label="Design tool badge"></div>

  <!-- Screen 1: Home -->
  <section class="screen screen-home">
    <div class="abs center site-logo" style="top:10px">RO INTERIORS</div>
    <div class="burger"><span></span><span></span><span></span></div>

    <div class="abs center hero-welcome" style="top:45px">Welcome</div>
    <div class="abs center hero-big" style="top:69px">INTERIOR</div>
    <div class="abs center hero-big" style="top:106px">STUDIO</div>
    <div class="photo" style="left:0;right:0;top:139px;height:170px;background:linear-gradient(160deg,#6d6c6e 0%,#4b4a4c 45%,#2f2e30 100%)" role="img" aria-label="Living room with fireplace and two round stools"></div>
    <div class="abs center hero-big white" style="top:143px">DESIGN</div>
    <div class="hero-rule" style="top:172px"></div>
    <div class="social-rail">
      <i style="top:14px"></i><i style="top:41px"></i><i style="top:67px"></i><i style="top:94px"></i>
    </div>

    <p class="abs body-copy" style="left:9px;right:10px;top:321px">Lorem ipsum dolor sit amet consectetur. Nulla amet dui condimentum urna quam tempus malesuada fames tellus. Enim viverra ipsum.</p>
    <div class="btn btn-lg" style="left:9px;top:393px;width:89px">Get Started</div>

    <div class="dark" style="top:430px;height:364px">
      <div class="abs eyebrow gold" style="left:19px;top:15px">Marla Venton</div>
      <div class="abs lead-title white" style="left:19px;top:25px;right:14px">Principle Lead Designer and RO Interiors Founder</div>
      <div class="abs caption white" style="left:19px;top:62px;right:14px">Marla is known for her passion in creating elegant and inviting spaces.</div>
      <div class="dots" style="left:9px;top:83px;width:22px;height:22px"></div>
      <div class="photo" style="left:19px;top:82px;width:120px;height:56px;background:linear-gradient(135deg,#4a4f58,#8a7a62 55%,#3b3d42)" role="img" aria-label="Home bar with wooden counter"></div>
      <div class="dots" style="left:141px;top:119px;width:10px;height:22px"></div>
      <div class="abs caption white" style="left:19px;top:150px;right:14px">She strives to keep interiors comfortable &amp; functional while introducing the classic trends in design.</div>
      <div class="dots" style="left:9px;top:192px;width:26px;height:22px"></div>
      <div class="photo" style="left:21px;top:193px;width:77px;height:117px;background:linear-gradient(160deg,#d8d2c8,#5b4f46 55%,#1f1e1f)" role="img" aria-label="Designer standing in a home office"></div>
      <div class="dots" style="left:103px;top:296px;width:26px;height:18px"></div>
      <div class="abs caption white" style="left:21px;top:322px;right:30px">She delivers creative elements, inspiration, and quality designs to a broad range of residential interiors, luxury apartments, and vacation homes.</div>
    </div>

    <div class="abs why-label" style="left:7px;top:806px">Why Choose Us?</div>
    <div class="abs why-heading" style="left:7px;top:822px;right:10px">Our goal was to create an impact and showcase our client's memorabilia.</div>
  </section>

  <!-- Screen 2: About & Services -->
  <section class="screen screen-about">
    <div class="dark" style="top:0;height:119px">
      <div class="photo" style="left:21px;top:0;width:92px;height:69px;background:linear-gradient(160deg,#d8d2c8,#5b4f46 55%,#1f1e1f)" role="img" aria-label="Designer standing in a home office"></div>
      <div class="dots" style="left:103px;top:55px;width:22px;height:20px"></div>
      <div class="abs caption white" style="left:21px;top:77px;right:40px">She delivers creative elements, inspiration, and quality designs to a broad range of residential interiors, luxury apartments, and vacation homes.</div>
    </div>

    <div class="abs why-label" style="left:8px;top:135px">Why Choose Us?</div>
    <div class="abs why-heading" style="left:8px;top:150px;right:8px">Our goal was to create an impact and showcase our client's memorabilia.</div>
    <div class="check" style="top:202px"><svg viewBox="0 0 10 10"><circle cx="5" cy="5" r="4.3" fill="none" stroke="#333" stroke-width=".8"/><path d="M3 5.2l1.4 1.4L7 3.8" fill="none" stroke="#333" stroke-width=".8"/></svg>Innovative Home Remodeling</div>
    <div class="check" style="top:219px"><svg viewBox="0 0 10 10"><circle cx="5" cy="5" r="4.3" fill="none" stroke="#333" stroke-width=".8"/><path d="M3 5.2l1.4 1.4L7 3.8" fill="none" stroke="#333" stroke-width=".8"/></svg>Exceptional Service</div>
    <div class="check" style="top:236px"><svg viewBox="0 0 10 10"><circle cx="5" cy="5" r="4.3" fill="none" stroke="#333" stroke-width=".8"/><path d="M3 5.2l1.4 1.4L7 3.8" fill="none" stroke="#333" stroke-width=".8"/></svg>The Modern Approach</div>
    <div class="btn btn-sm" style="left:8px;top:253px;width:35px">Learn More</div>
    <div class="dots" style="left:7px;top:275px;width:22px;height:22px"></div>
    <div class="photo" style="left:20px;top:285px;width:56px;height:94px;background:linear-gradient(150deg,#c06a3a,#8a5336 50%,#d9c6a8)" role="img" aria-label="Living room with copper accent wall"></div>
    <div class="photo" style="left:79px;top:310px;width:57px;height:94px;background:linear-gradient(150deg,#e9e1d6,#bfae97 60%,#8f8272)" role="img" aria-label="Bright room under renovation"></div>
    <div class="dots" style="left:122px;top:392px;width:22px;height:22px"></div>

    <div class="dark services-bg" style="top:429px;height:492px" role="img" aria-label="Dusk view of a brick house behind the services list">
      <div class="abs center svc-title gold" style="top:15px">Our Services</div>
      <div class="abs center svc-lead white" style="top:40px;left:8px;right:8px">Our brief was to create an inviting home that highlighted the furniture selections to cater to the growing family.</div>
      <svg class="abs" style="left:56px;top:144px" width="46" height="46" viewBox="0 0 46 46"><g fill="var(--gold)"><rect x="19" y="-3" width="9" height="52" rx="1" transform="rotate(45 23 23)"/><rect x="19" y="-3" width="9" height="52" rx="1" transform="rotate(-45 23 23)"/></g></svg>
      <div class="abs center svc-name white" style="top:202px">RESIDENTIAL DESIGN</div>
      <div class="abs center svc-copy white" style="top:233px;left:14px;right:14px">Lorem ipsum dolor sit amet consectetur. Venenatis laoreet aenean ut molestie felis.</div>
      <div class="abs center see-more gold" style="top:286px">See More &nbsp;›</div>
      <svg class="abs" style="left:54px;top:314px" width="52" height="40" viewBox="0 0 52 40"><path d="M2 40V16L22 2l28 12v26H34V24h-8v16z" fill="var(--gold)"/><path d="M8 38V19l14-10 22 10v19" fill="none" stroke="#3b3532" stroke-width="2"/></svg>
      <div class="abs center svc-name white" style="top:370px">INTERIOR DICORATING</div>
      <div class="abs center svc-copy white" style="top:401px;left:14px;right:14px">Lorem ipsum dolor sit amet consectetur. Venenatis laoreet aenean ut molestie felis.</div>
      <div class="abs center see-more gold" style="top:454px">See More &nbsp;›</div>
      <svg class="abs" style="left:66px;top:478px" width="26" height="14" viewBox="0 0 26 14"><rect x="8" y="4" width="12" height="10" fill="var(--gold)"/><rect x="2" y="6" width="3" height="3" fill="var(--gold)"/></svg>
    </div>
  </section>

  <!-- Screen 3: Portfolio & Footer -->
  <section class="screen screen-footer">
    <div class="dark services-bg" style="top:0;height:236px" role="img" aria-label="Dusk view of a brick house behind the services list">
      <div class="abs center svc-copy white" style="top:-1px;left:14px;right:14px">aenean ut molestie felis.</div>
      <div class="abs center see-more gold" style="top:25px">See More &nbsp;›</div>
      <svg class="abs" style="left:55px;top:51px" width="50" height="46" viewBox="0 0 50 46"><rect x="16" y="6" width="22" height="14" rx="2" transform="rotate(35 27 13)" fill="var(--gold)"/><rect x="26" y="24" width="5" height="22" rx="2" transform="rotate(-35 28 35)" fill="var(--gold)"/><rect x="4" y="10" width="4" height="4" fill="var(--gold)"/><rect x="10" y="4" width="3" height="3" fill="var(--gold)"/><rect x="9" y="16" width="4" height="4" fill="var(--gold)"/></svg>
      <div class="abs center svc-name white" style="top:108px;line-height:1.5">RENOVATING &amp;<br>REMODELING</div>
      <div class="abs center svc-copy white" style="top:150px;left:14px;right:14px">Lorem ipsum dolor sit amet consectetur. Venenatis laoreet aenean ut molestie felis.</div>
      <div class="abs center see-more gold" style="top:193px">See More &nbsp;›</div>
    </div>

    <div class="abs center port-title" style="top:253px">Portofolio</div>
    <div class="abs center port-copy" style="top:275px;left:8px;right:8px">The studio provided our client with a welcoming home office that suited his needs.</div>
    <div class="photo" style="left:9px;top:354px;width:140px;height:107px;background:linear-gradient(160deg,#6f7268,#3d3b38 50%,#1d1c1c)" role="img" aria-label="Dark wood home office with coffered ceiling"></div>
    <div class="abs center carousel-label white" style="top:397px">RESIDENTIAL DESIGN</div>
    <div class="abs center gold" style="top:410px;font-size:5px">See More ›</div>
    <div class="arrow-dot" style="left:5px;top:403px"></div>
    <div class="arrow-dot" style="left:146px;top:403px"></div>

    <div class="abs site-logo" style="left:9px;top:508px">RO INTERIORS</div>
    <div class="abs foot-small" style="left:9px;top:523px;right:20px">Serving the Birchwood Valley and surrounding areas, Birchwood Valley, NY</div>
    <div class="abs" style="left:9px;top:548px;font-size:6.8px;font-weight:600">Subscribe for Update Newsletter</div>
    <div class="input" style="left:9px;top:562px;width:86px">Enter your email</div>
    <div class="btn btn-sm" style="left:116px;top:562px;width:33px;height:12px;line-height:12px">Learn More</div>

    <div class="dark" style="top:590px;height:247px">
      <div class="abs foot-head white" style="left:9px;top:15px">NAVIGATION</div>
      <div class="abs foot-head white" style="left:77px;top:15px">LEGAL</div>
      <div class="abs foot-link white" style="left:9px;top:36px">Home<br>About<br>Our Services<br>Contact Us</div>
      <div class="abs foot-link white" style="left:77px;top:36px">General Info<br>Privacy<br>Terms Of Services</div>
      <div class="abs foot-head white" style="left:9px;top:107px">TALK TO US</div>
      <div class="abs foot-head white" style="left:83px;top:107px">Schedule</div>
      <div class="abs foot-link white" style="left:9px;top:129px">555-013-2847<br>hello@ro.example<br>Friendbook<br>Snapshots</div>
      <div class="abs white" style="left:83px;top:133px;font-size:7.2px;line-height:1.5;width:70px">Mon - Fri | 9 a.m - 5 p.m</div>
      <div class="abs white" style="left:83px;top:164px;font-size:7.2px">Sat &amp; Sun | Closed</div>
      <div class="foot-rule" style="top:203px"></div>
      <div class="abs center white" style="top:218px;font-size:8.6px">Copyright © 2023 RO Interiors LLC</div>
    </div>
  </section>

</body>
</html>
```